Brenton High 20 year Reunion Memorial

I need a tasteful memorial poster with the names of those alumni that have deceased. The school colors are black, orange, silver and white. I would definately like the background to be black. At the top of the poster I would like it to read:
Brenton Hight School Class of 1993.
This evening is dedicated in memory of
(followed by the names on the attached file

Industry/Entity Type

School

Requirements
Must have
• Black background

```html
<!DOCTYPE html>
<html lang="en">
<head>
<meta charset="utf-8">
<title>Brenton High School Class of 1993 – Memorial</title>
<link rel="stylesheet" href="https://fonts.googleapis.com/css2?family=Noto+Serif:wght@400&display=swap">
<style>
  :root {
    --black: #050505;
    --orange: #f59f12;
    --white: #f4f4f4;
    --silver-light: #f2f4f4;
    --silver-mid: #b9c4c4;
    --silver-dark: #8f9c9c;
  }
  html, body {
    margin: 0;
    padding: 0;
    width: 800px;
    height: 1200px;
    overflow: hidden;
    background: var(--silver-mid);
  }
  .poster {
    position: relative;
    width: 800px;
    height: 1200px;
    background: linear-gradient(120deg, var(--silver-dark) 0%, var(--silver-light) 12%, var(--silver-mid) 30%, var(--silver-light) 55%, var(--silver-dark) 75%, var(--silver-light) 100%);
    font-family: "Noto Serif", Georgia, serif;
  }
  .panel {
    position: absolute;
    left: 45px;
    top: 45px;
    width: 710px;
    height: 1110px;
    background: radial-gradient(ellipse at 50% 40%, #141414 0%, var(--black) 75%);
  }
  .emblem {
    position: absolute;
    left: 0;
    width: 800px;
    top: 178px;
    display: flex;
    justify-content: center;
    align-items: center;
    gap: 12px;
    color: var(--white);
    font-size: 20px;
    letter-spacing: 3px;
    text-transform: uppercase;
  }
  .emblem-dot {
    width: 14px;
    height: 14px;
    border-radius: 50%;
    background: var(--white);
  }
  .school-name {
    position: absolute;
    left: 0;
    width: 800px;
    top: 306px;
    margin: 0;
    text-align: center;
    color: var(--orange);
    font-weight: 400;
    font-size: 52px;
    font-variant: small-caps;
    letter-spacing: 3px;
    line-height: 1;
  }
  .class-year {
    position: absolute;
    left: 0;
    width: 800px;
    top: 378px;
    margin: 0;
    text-align: center;
    color: var(--orange);
    font-weight: 400;
    font-size: 31px;
    letter-spacing: 3px;
    line-height: 1;
  }
  .rule {
    position: absolute;
    left: 196px;
    width: 417px;
    height: 1px;
    background: var(--white);
  }
  .rule-top { top: 441px; }
  .rule-bottom { top: 489px; }
  .dedication {
    position: absolute;
    left: 0;
    width: 800px;
    top: 456px;
    margin: 0;
    text-align: center;
    color: var(--white);
    font-size: 16.5px;
    letter-spacing: 2.6px;
    line-height: 1;
  }
  .memorial-list {
    list-style: none;
    margin: 0;
    padding: 0;
  }
  .memorial-entry {
    position: absolute;
    left: 0;
    width: 800px;
    height: 60px;
  }
  .entry-name {
    position: absolute;
    top: 0;
    color: var(--orange);
    font-size: 19px;
    letter-spacing: 2px;
    line-height: 1;
    white-space: nowrap;
  }
  .entry-dates {
    position: absolute;
    top: 27px;
    left: 265px;
    color: var(--white);
    font-size: 15.5px;
    letter-spacing: 2.2px;
    line-height: 1;
    white-space: nowrap;
  }
</style>
</head>
<body>
<main class="poster">
  <div class="panel"></div>

  <div class="emblem" aria-label="Brenton High emblem">
    <span class="emblem-dot"></span>
    <span>Brenton High</span>
  </div>

  <h1 class="school-name">Brenton High School</h1>
  <h2 class="class-year">CLASS OF 1993</h2>

  <div class="rule rule-top"></div>
  <p class="dedication">THIS EVENING DEDICATED IN LOVING MEMORY OF</p>
  <div class="rule rule-bottom"></div>

  <ul class="memorial-list">
    <li class="memorial-entry" style="top:553px">
      <span class="entry-name" style="left:167px">RACHEL DUNMORE</span>
      <span class="entry-dates">MARCH 3, 1975 - OCTOBER 14, 1993</span>
    </li>
    <li class="memorial-entry" style="top:632px">
      <span class="entry-name" style="left:194px">STEVEN PRATT</span>
      <span class="entry-dates">APRIL 11, 1975 - JULY 19, 1998</span>
    </li>
    <li class="memorial-entry" style="top:711px">
      <span class="entry-name" style="left:207px">ALAN KESSLER</span>
      <span class="entry-dates">MARCH 15, 1975 - MAY 8, 2003</span>
    </li>
    <li class="memorial-entry" style="top:790px">
      <span class="entry-name" style="left:182px">LUCAS FERREIRA</span>
      <span class="entry-dates">AUGUST 17, 1975 - FEBRUARY 9, 2009</span>
    </li>
    <li class="memorial-entry" style="top:869px">
      <span class="entry-name" style="left:177px">INGRID HALVORSEN</span>
      <span class="entry-dates">JUNE 21, 1975 - OCTOBER 2, 2011</span>
    </li>
    <li class="memorial-entry" style="top:948px">
      <span class="entry-name" style="left:150px">PAULA WHITFIELD</span>
      <span class="entry-dates">JANUARY 12, 1975 - NOVEMBER 18, 2012</span>
    </li>
    <li class="memorial-entry" style="top:1027px">
      <span class="entry-name" style="left:213px">DEREK HANLON</span>
      <span class="entry-dates">APRIL 6, 1975 - JANUARY 14, 2014</span>
    </li>
  </ul>
</main>
</body>
</html>
```